Design for new site

Hi, we need a web design for a new product calmridgeway.
This product is aimed to help people with anxiety, panic attacks and other disorders on permanently basis.
Please take a look at competitors web-sites:
http://www.brightharborpath.example/
http://www.stillmeadow.example/
Key Audiences
The intended audience for this site will be people that are looking for relief from panic and anxiety.
Key Objectives
Key object is to get prospective clients to sign up for membership and purchase our audio course.
Theme of Site
The general site theme needs to be clean and simple. The audience coming to the site in under a lot of anxiety and we don’t want to add any stress.
The site needs to flow easy from top down, with few distractions in side menus and/or columns.
Color Scheme
Suggested colors need to be light shades of blue. Blue psychology is tranquil, peaceful, and calm. This color has a tremendous stress management quality to it, making us feel cool and calm.
Or it can be shades of cool green of summer forest.
Please take a look at site mock up in attachment.

```html
<!DOCTYPE html>
<html lang="en">
<head>
<meta charset="utf-8">
<title>CalmridgeWay</title>
<link href="https://fonts.googleapis.com/css2?family=Varela+Round&family=Open+Sans:ital,wght@0,400;0,600;1,400&display=swap" rel="stylesheet">
<style>
:root{
  --sky:#2bb8e4;
  --sky-light:#c9f0fd;
  --sky-deep:#3ab9f2;
  --ink-blue:#18506b;
  --green:#66a81c;
  --text:#4a4a4a;
  --muted:#7a7a7a;
  --line:#dcdcdc;
  --footer:#f5f5f5;
  --white:#ffffff;
}
*{margin:0;padding:0;box-sizing:border-box}
html,body{width:798px;height:1200px;overflow:hidden;background:var(--white)}
body{position:relative;font-family:"Open Sans",sans-serif;color:var(--text)}
.abs{position:absolute}
.round{font-family:"Varela Round",sans-serif}

.site-header{position:absolute;left:0;top:0;width:798px;height:67px;border-bottom:1px solid var(--line)}
.logo{left:80px;top:24px;font-size:23px;color:var(--sky)}
.phone{left:612px;top:35px;font-size:14px;color:var(--green);display:flex;align-items:center;gap:4px}

.main-nav{top:67px;left:0;width:798px;height:32px;background:linear-gradient(#fff,#efefef);border-bottom:1px solid #e2e2e2}
.main-nav a{position:absolute;top:8px;font-size:12px;color:#444;text-decoration:none;transform:translateX(-50%);white-space:nowrap}
.nav-sep{position:absolute;top:0;width:1px;height:32px;background:#d8d8d8}

.hero{top:99px;left:0;width:798px;height:310px;background:radial-gradient(ellipse 360px 200px at 220px 130px,var(--sky-light),transparent 80%),linear-gradient(#48d0fb,var(--sky-deep))}
.hero-kicker{left:78px;top:90px;font-size:19px;color:var(--sky)}
.hero-title{left:77px;top:116px;font-size:25px;color:var(--ink-blue)}
.hero-text{left:80px;top:155px;width:300px;font-size:8.5px;line-height:14px;color:#2a7fa8}
.dot{position:absolute;top:193px;width:10px;height:10px;border-radius:50%;background:var(--white)}
.dot.active{background:#000}
.hero-photo{left:421px;top:56px;width:293px;height:194px;border-radius:16px;background:var(--white);padding:4px}
.hero-photo div{width:100%;height:100%;border-radius:12px;background:linear-gradient(#dfeef2 0%,#e8e0b8 35%,#c9a64f 70%,#9c7a2e 100%)}

.welcome{left:0;top:440px;width:798px;text-align:center}
.welcome h1{font-weight:400;font-size:20px;color:#444}
.welcome h2{font-weight:400;font-size:13px;color:#666;margin-top:4px}
.welcome p{width:600px;margin:10px auto 0;font-size:8.5px;line-height:15px;color:#777}
.divider{left:77px;top:564px;width:644px;height:1px;background:#e3e3e3}

.card{position:absolute;top:594px;width:209px;height:183px;border:1px solid #e2e2e2;border-radius:3px;background:var(--white);box-shadow:0 8px 10px -8px rgba(0,0,0,.15)}
.card-media{position:absolute;left:0;top:0;width:100%;height:96px;border-bottom:1px solid #e2e2e2}
.card h3{position:absolute;left:11px;font-weight:400;font-size:16px;color:var(--sky)}
.card p{position:absolute;left:11px;width:190px;font-size:7.5px;line-height:12.5px;color:#777}
.play{position:absolute;left:89px;top:42px;width:30px;height:30px;border-radius:50%;background:var(--white)}

.testimonials-title{left:0;top:819px;width:798px;text-align:center;font-size:20px;color:var(--green);font-weight:400}
.avatar{position:absolute;width:70px;height:70px;border-radius:50%;background:linear-gradient(#8a6c5a,#d9b9a4);box-shadow:0 10px 8px -8px rgba(0,0,0,.2)}
.quote-mark{position:absolute;font-size:22px;color:#777;font-family:Georgia,serif;line-height:1}
.quote{position:absolute;width:188px;font-style:italic;font-size:7.5px;line-height:12.5px;color:#777}
.author{position:absolute;font-size:8.5px;color:#333}

.site-footer{left:0;top:996px;width:798px;height:162px;background:var(--footer);border-top:1px solid #e2e2e2}
.footer-col{position:absolute;top:30px}
.footer-col h4{font-weight:400;font-size:13px;color:#444;margin-bottom:6px}
.footer-col a{display:block;font-size:8.5px;line-height:15.7px;color:#555;text-decoration:none}
.social{display:flex;gap:6px;margin-top:2px}
.social span{width:17px;height:17px;background:var(--sky);border-radius:2px}
.bottom-bar{left:0;top:1158px;width:798px;height:42px;border-top:1px solid #e2e2e2}
.copyright{left:97px;top:13px;font-size:8px;color:#777}
</style>
</head>
<body>

<header class="site-header">
  <div class="abs logo round">CalmridgeWay</div>
  <div class="abs phone round">
    <svg width="14" height="14" viewBox="0 0 14 14"><circle cx="7" cy="7" r="6.3" fill="none" stroke="#999" stroke-width="1"/><path d="M4.6 3.8c.4-.3.8-.2 1 .2l.6 1.1c.2.4 0 .7-.3.9-.3.2-.3.4-.1.8.4.7.9 1.2 1.6 1.6.3.2.6.2.8-.1.2-.3.5-.5.9-.3l1.1.6c.4.2.5.6.2 1-.8 1-2 .9-3.4-.1-1.4-1-2.4-2.5-2.6-3.7-.1-.8.2-1.6.2-2z" fill="#999"/></svg>
    555.014.2270
  </div>
</header>

<nav class="abs main-nav round">
  <a style="left:117px">Home</a>
  <span class="nav-sep" style="left:148px"></span>
  <a style="left:187px">Product</a>
  <span class="nav-sep" style="left:223px"></span>
  <a style="left:282px">Success Stories</a>
  <span class="nav-sep" style="left:337px"></span>
  <a style="left:387px">Anxiety Test</a>
  <span class="nav-sep" style="left:435px"></span>
  <a style="left:466px">Blog</a>
  <span class="nav-sep" style="left:492px"></span>
  <a style="left:529px">About</a>
  <span class="nav-sep" style="left:560px"></span>
  <a style="left:591px">FAQ</a>
  <span class="nav-sep" style="left:618px"></span>
  <a style="left:665px">Contact Us</a>
</nav>

<section class="abs hero">
  <div class="abs hero-kicker round">Mauris vel lacus vitae felis</div>
  <div class="abs hero-title round">Sed metus augue convallis</div>
  <p class="abs hero-text">Vivamus porttitor purus nisi eleifend libero a tempus libero lectus feugiat felis Morbi diam mauris viverra in gravida eu ma</p>
  <span class="dot active" style="left:78px"></span>
  <span class="dot" style="left:90px"></span>
  <span class="dot" style="left:101px"></span>
  <span class="dot" style="left:113px"></span>
  <div class="abs hero-photo"><div role="img" aria-label="Photo of a woman with open arms in a sunlit wheat field"></div></div>
</section>

<section class="abs welcome round">
  <h1>Welcome to Calm Ridge Way Mainpage</h1>
  <h2>Vivamus porttitor purus nisi eleifend libero tempus</h2>
  <p style="font-family:'Open Sans',sans-serif">Morbi ornare gravida elit Integer congue augue et malesuada iaculis ipsum dui aliquet felis at cursus magna nisl nec elit Praesent elementum elit at tellus nec ultricies sit amet porttitor mattis enim In massa libero interdum nec interdum vel blandit sed nulla In ullamcorper est eget tempor cursus neque mi consectetuer mi a ultricies massa est sed nisl Class aptent taciti sociosqu ad litora torquent per conubia nostra per</p>
</section>
<div class="abs divider"></div>

<article class="card" style="left:77px">
  <div class="card-media" role="img" aria-label="Product photo of the audio course box set and discs" style="background:linear-gradient(135deg,#f4f6fa,#dfe6f2 50%,#f6f7fa)"></div>
  <h3 class="round" style="top:102px">Our Product</h3>
  <p style="top:124px">Morbi porta libero id ullamcorper nonummy nibh ligula pulvinar metus eget consectetuer augue nisi quis lacus Ut ac mi commodo</p>
</article>

<article class="card" style="left:294px">
  <div class="card-media" role="img" aria-label="Photo of a stressed man sitting with his head in his hand" style="background:linear-gradient(#3a2a20,#7a5434 60%,#2c2018)"></div>
  <h3 class="round" style="top:105px">Anxiety Test</h3>
  <p style="top:126px">Morbi porta libero id ullamcorper nonummy nibh ligula pulvinar metus eget consectetuer augue nisi quis lacus Ut ac mi</p>
</article>

<article class="card" style="left:511px;height:179px">
  <div role="img" aria-label="Video still of two women talking at a table" style="position:absolute;left:8px;top:7px;width:193px;height:115px;border-radius:2px;background:linear-gradient(90deg,#c9c4bc,#e3ded6 50%,#b9b3a8)">
    <span class="play"></span>
    <svg style="position:absolute;left:100px;top:51px" width="10" height="12" viewBox="0 0 10 12"><path d="M1 0l9 6-9 6z" fill="#111"/></svg>
  </div>
  <h3 class="round" style="top:131px;font-size:14.5px">Watch Our latest Video</h3>
  <p class="round" style="top:153px;font-size:10px;color:#555">Nunc porta convallis pede</p>
</article>

<h2 class="abs testimonials-title round">Testimonials</h2>

<div class="avatar" role="img" aria-label="Portrait of a smiling woman" style="left:112px;top:867px"></div>
<span class="quote-mark" style="left:178px;top:865px">&ldquo;</span>
<p class="quote" style="left:194px;top:871px">Vivamus porttitor purus nisi eleifend libero a tempus libero lectus feugiat felis Morbi diam mauris viverra in gravida eu mattis in ante Morbi eget arcu Morbi porta libero id ullamcorper nonummy nibh ligul</p>
<span class="author" style="left:194px;top:924px">By Author Name</span>

<div class="avatar" role="img" aria-label="Portrait of a smiling man" style="left:408px;top:865px"></div>
<span class="quote-mark" style="left:477px;top:863px">&ldquo;</span>
<p class="quote" style="left:493px;top:868px">Vivamus porttitor purus nisi eleifend libero a tempus libero lectus feugiat felis Morbi diam mauris viverra in gravida eu mattis in ante Morbi eget arcu Morbi porta libero id ullamcorper nonummy nibh ligul</p>
<span class="author" style="left:493px;top:917px">By Author Name</span>

<footer class="abs site-footer">
  <div class="footer-col" style="left:102px">
    <h4 class="round">Quick Links</h4>
    <a>About Us</a><a>Success Stories</a><a>Anixiety Test</a><a>Recent Blog</a><a>FAQ</a>
  </div>
  <div class="footer-col" style="left:232px">
    <h4 class="round">Products</h4>
    <a>Vivamus porttitor</a><a>Purus nisi eleifend</a><a>Libero tempus</a><a>Feugiat felis</a><a>Morbi diam</a>
  </div>
  <div class="footer-col" style="left:362px">
    <h4 class="round">Resources</h4>
    <a>Vivamus porttitor</a><a>Purus nisi eleifend</a><a>Libero tempus</a><a>Feugiat felis</a><a>Morbi diam</a>
  </div>
  <div class="footer-col" style="left:492px">
    <h4 class="round">Support</h4>
    <a>Term of Use</a><a>Support</a><a>Sitemap</a><a>Contact Us</a>
  </div>
  <div class="footer-col" style="left:592px">
    <h4 class="round">Get in touch</h4>
    <div class="social"><span></span><span></span><span></span><span></span></div>
  </div>
</footer>

<div class="abs bottom-bar">
  <span class="abs copyright">© 2014 Company Name&nbsp; All right reserved&nbsp; Term of Use</span>
</div>

</body>
</html>
```